KORBALT

The business want a professional looking business card. We have a scetch we will add but want the extra upgrade, and would like more suggestions for variations of our business cards.

```html
<!DOCTYPE html>
<html lang="en">
<head>
<meta charset="utf-8">
<title>KORBALT business card</title>
<link href="https://fonts.googleapis.com/css2?family=Cinzel:wght@500;600&family=Montserrat:wght@500;700&display=swap" rel="stylesheet">
<style>
  :root {
    --backdrop: #68686a;
    --card-light: #ebe4d2;
    --card-mid: #d2b76e;
    --card-deep: #74551f;
    --gold: #b38a2c;
    --gold-bright: #caa445;
    --ink: #3a2a10;
    --pattern-tone: rgba(214, 178, 80, 0.28);
  }
  * { margin: 0; padding: 0; box-sizing: border-box; }
  html, body { width: 900px; height: 1200px; overflow: hidden; }
  body { background: var(--backdrop); position: relative; }

  .card {
    position: absolute;
    left: 136px;
    width: 630px;
    height: 357px;
    border-radius: 14px;
    overflow: hidden;
    background: linear-gradient(90deg, var(--card-light) 0%, var(--card-mid) 50%, var(--card-deep) 100%);
  }
  .card--front { top: 216px; }
  .card--back { top: 630px; }

  .pattern-field {
    position: absolute; inset: 0;
    background: linear-gradient(90deg, rgba(255,255,255,0.05), var(--pattern-tone), rgba(120,80,20,0.12));
  }

  .front-brand {
    position: absolute; left: 0; right: 0; top: 130px;
    text-align: center;
  }
  .front-brand__name {
    font-family: "Cinzel", serif; font-weight: 500;
    font-size: 64px; letter-spacing: 0.2em; line-height: 1;
    color: var(--gold); padding-left: 0.2em;
  }
  .front-brand__since {
    margin-top: 22px;
    font-family: "Cinzel", serif; font-weight: 600;
    font-size: 15px; letter-spacing: 0.5em; color: #8d7440; padding-left: 0.5em;
  }

  .holder { position: absolute; left: 49px; top: 60px; }
  .holder__company {
    font-family: "Cinzel", serif; font-weight: 500;
    font-size: 30px; line-height: 1; color: var(--gold-bright); letter-spacing: 0.01em;
  }
  .holder__role {
    margin-top: 18px;
    font-family: "Montserrat", sans-serif; font-weight: 500;
    font-size: 21px; color: var(--ink);
  }
  .holder__person {
    margin-top: 8px;
    font-family: "Montserrat", sans-serif; font-weight: 700;
    font-size: 21px; color: var(--gold);
  }

  .contacts { position: absolute; left: 49px; top: 214px; list-style: none; }
  .contacts li {
    display: flex; align-items: center; gap: 6px;
    height: 30px;
    font-family: "Montserrat", sans-serif; font-weight: 500;
    font-size: 18.5px; color: var(--ink);
  }
  .contacts svg { width: 12px; height: 12px; fill: none; stroke: var(--ink); stroke-width: 1.6; }

  .back-brand { position: absolute; left: 371px; top: 120px; width: 210px; text-align: center; }
  .back-brand__dot {
    display: block; margin: 0 auto 26px;
    width: 60px; height: 60px; border-radius: 50%;
    background: var(--gold-bright);
  }
  .back-brand__name {
    font-family: "Cinzel", serif; font-weight: 500;
    font-size: 31px; letter-spacing: 0.18em; line-height: 1;
    color: var(--gold-bright); padding-left: 0.18em;
  }
  .back-brand__since {
    margin-top: 6px;
    font-family: "Cinzel", serif; font-weight: 600;
    font-size: 10px; letter-spacing: 0.5em; color: #8a6c30; padding-left: 0.5em;
  }
</style>
</head>
<body>
  <section class="card card--front">
    <div class="pattern-field" role="img" aria-label="Repeating gold floral ornament pattern across the card face"></div>
    <div class="front-brand">
      <div class="front-brand__name">KORBALT</div>
      <div class="front-brand__since">SINCE 2026</div>
    </div>
  </section>

  <section class="card card--back">
    <div class="holder">
      <div class="holder__company">KORBALT H VOLDHEIM</div>
      <div class="holder__role">CEO &amp; Founder</div>
      <div class="holder__person">Lars Henrik Voldheim</div>
    </div>

    <ul class="contacts">
      <li>
        <svg viewBox="0 0 12 12" aria-hidden="true"><rect x="3" y="0.8" width="6" height="10.4" rx="1"/><line x1="5" y1="9.4" x2="7" y2="9.4"/></svg>
        004791234567
      </li>
      <li>
        <svg viewBox="0 0 12 12" aria-hidden="true"><rect x="0.8" y="2.5" width="10.4" height="7" rx="0.6"/><polyline points="0.8,2.8 6,6.6 11.2,2.8"/></svg>
        korbalt.llc@mailbox.com
      </li>
      <li>
        <svg viewBox="0 0 12 12" aria-hidden="true"><circle cx="6" cy="6" r="5"/><ellipse cx="6" cy="6" rx="2.2" ry="5"/><line x1="1" y1="6" x2="11" y2="6"/></svg>
        www.korbalt.llc
      </li>
    </ul>

    <div class="back-brand">
      <span class="back-brand__dot"></span>
      <div class="back-brand__name">KORBALT</div>
      <div class="back-brand__since">SINCE 2026</div>
    </div>
  </section>
</body>
</html>
```